Salon and Spa Distributor Business Card

Need a business card. We are are distributor in the salon and spa industry. We identify with natural beauty. Need a card with:
Company Name: Petal Haven"
Title: "President & CEO"
Address
Company Phone number
email
website
Tag Line:" Pure Supplies for Every Salon"

Industry/Entity Type

Business

Contact Information for Business Card

Name: Lena Morcott
Title: "President & CEO"
Address: 317 Birchfield Ln, Oakvane, NJ 07481
Company Phone number: 800-463-9152
email: lenamorcott@petalhaven-example.com
website: www.petalhaven-example.com

Requirements
Should not have
• No black backgrounds

```html
<!DOCTYPE html>
<html lang="en">
<head>
<meta charset="utf-8">
<title>Petal Haven – Business Card</title>
<link href="https://fonts.googleapis.com/css2?family=Questrial&family=Source+Sans+3:wght@400&display=swap" rel="stylesheet">
<style>
  :root {
    --green-light: #63b946;
    --green-dark: #2c8438;
    --green-ink: #2a7a33;
    --green-brand: #5cb545;
    --green-haze: #a9da8f;
    --white: #ffffff;
  }
  * { margin: 0; padding: 0; box-sizing: border-box; }
  html, body { width: 1200px; height: 720px; overflow: hidden; background: var(--white); }
  .card {
    position: relative;
    width: 1200px;
    height: 720px;
    overflow: hidden;
    font-family: "Questrial", sans-serif;
  }
  .card-backdrop { position: absolute; inset: 0; width: 1200px; height: 720px; }
  .brand-mark {
    position: absolute;
    left: 120px;
    top: 120px;
    width: 160px;
    height: 160px;
    border-radius: 50%;
    background: var(--green-brand);
  }
  .company-name {
    position: absolute;
    left: 360px; width: 720px;
    top: 34px;
    text-align: center;
    font-size: 78px;
    font-weight: 400;
    color: var(--green-brand);
    line-height: 1;
  }
  .tagline {
    position: absolute;
    left: 340px; width: 760px;
    top: 142px;
    text-align: center;
    font-size: 45px;
    color: var(--green-brand);
    line-height: 1;
  }
  .job-title {
    position: absolute;
    left: 360px; width: 720px;
    top: 285px;
    text-align: center;
    font-family: "Source Sans 3", sans-serif;
    font-size: 76px;
    color: var(--green-ink);
    line-height: 1;
  }
  .contact {
    position: absolute;
    left: 0; width: 1264px;
    top: 594px;
    text-align: center;
    color: var(--white);
    font-style: normal;
    font-size: 30px;
    line-height: 45px;
  }
  .contact .sep { margin: 0 14px; }
</style>
</head>
<body>
  <div class="card">
    <svg class="card-backdrop" viewBox="0 0 1200 720" aria-hidden="true">
      <defs>
        <linearGradient id="edgeHaze" x1="0" y1="0" x2="1" y2="0">
          <stop offset="0" stop-color="var(--green-haze)"/>
          <stop offset="0.12" stop-color="var(--white)"/>
          <stop offset="1" stop-color="var(--white)"/>
        </linearGradient>
      </defs>
      <rect class="field-light" width="1200" height="720" fill="var(--green-light)"/>
      <path class="swoosh-white" d="M0 0 H1080 C1190 70 1215 210 1150 310 C1070 430 830 478 600 476 C360 474 150 420 0 362 Z" fill="url(#edgeHaze)"/>
      <path class="band-dark" d="M0 410 C260 520 620 562 880 522 C1000 502 1110 462 1200 422 V720 H0 Z" fill="var(--green-dark)"/>
      <path class="swoosh-crescent" d="M860 484 C1000 442 1140 342 1200 222 V300 C1120 410 1000 472 860 484 Z" fill="var(--green-light)"/>
    </svg>

    <div class="brand-mark" aria-hidden="true"></div>
    <h1 class="company-name">Petal Haven</h1>
    <p class="tagline">Pure Supplies for Every Salon</p>
    <p class="job-title">President &amp; CEO</p>

    <address class="contact">
      <div class="contact-line">317 Birchfield Ln, Oakvane, NJ 07481<span class="sep">·</span>800-463-9152</div>
      <div class="contact-line">lenamorcott@petalhaven-example.com<span class="sep">·</span>www.petalhaven-example.com</div>
    </address>
  </div>
</body>
</html>
```